New emergency medical service needs a marketing flyer for prospective customers

We need a tri fold brochure on an 8.5 X 11 stock for a new emergency medical service in Pennsylvania. We provide basic first aid and now Covid-19 pre screening and temperature monitoring for special events, large gatherings and businesses. Examples of these would be but not limited to: Sporting events, carnivals, festivals, craft shows, warehouses, churches, manufacturing facilities, industrial buildings, large construction sites, multi occupancy officer buildings. The market for this is pretty much untouched and endless. we would like to use gray as the back ground color and obviously our logo. The final design should grab their attention and communicate the importance of having trained and certified professionals at their event or facility. We want to give them that piece of mind they are in good hands with us.

Target Market(s)

primary focus is going to be on businesses with large offices, large buildings or lots of foot traffic in and out of the building

Requirements
Must have
• gray background, pictures, company phone # , company web site, and contact email address. I will provide all that information to the winner to add at the end.
Nice to have
• pictures that covers the whole front cover with logo at top

```html
<!DOCTYPE html>
<html lang="en">
<head>
<meta charset="utf-8">
<title>Arven Medical Services – Tri-fold Brochure</title>
<link href="https://fonts.googleapis.com/css2?family=Montserrat:wght@700;800&family=Open+Sans:wght@400;600&display=swap" rel="stylesheet">
<style>
  :root {
    --navy: #253589;
    --teal: #13b5c2;
    --sheet-gray: #e4e4e4;
    --pattern-gray: #d6d6d6;
    --panel-dark: #4d4c4c;
    --body-gray: #555555;
    --white: #ffffff;
  }
  * { margin: 0; padding: 0; box-sizing: border-box; }
  html, body { width: 1200px; height: 928px; overflow: hidden; background: var(--sheet-gray); }
  .brochure {
    position: relative; width: 1200px; height: 928px; overflow: hidden;
    background: var(--sheet-gray);
    font-family: "Open Sans", Arial, sans-serif;
  }
  .headline {
    font-family: "Montserrat", Arial, sans-serif; font-weight: 800;
    text-transform: uppercase; position: absolute; white-space: nowrap;
  }

  /* Left panel */
  .safety-title {
    left: 28px; top: 40px; color: var(--navy);
    font-size: 61px; line-height: 72.5px; letter-spacing: -1px;
  }
  .care-photo {
    position: absolute; left: 0; top: 350px; width: 400px; height: 416px;
    border-radius: 0 52px 52px 0;
    background: linear-gradient(135deg, #8ccdd4 0%, #6fb6bd 45%, #7cc2ca 100%);
    overflow: hidden; z-index: 1;
  }
  .care-copy {
    position: absolute; left: 29px; top: 36px; width: 334px;
    color: var(--white); font-size: 15.4px; line-height: 18.2px;
  }
  .care-copy p + p { margin-top: 18px; }
  .pill-pattern {
    position: absolute; left: 0; top: 766px; width: 400px; height: 162px;
    background: linear-gradient(180deg, var(--pattern-gray) 0%, var(--sheet-gray) 100%);
  }

  /* Middle panel */
  .brand-pill {
    position: absolute; left: 400px; top: 76px; width: 400px; height: 161px;
    background: var(--white); border-radius: 80px 0 0 80px;
    display: flex; align-items: center; justify-content: center; gap: 12px;
    padding-left: 30px;
  }
  .brand-dot { width: 24px; height: 24px; border-radius: 50%; background: var(--navy); flex: none; }
  .brand-name {
    font-family: "Montserrat", Arial, sans-serif; font-weight: 800;
    color: var(--navy); font-size: 24px; letter-spacing: -0.3px; white-space: nowrap;
  }
  .service-title {
    left: 429px; top: 342px; color: var(--navy);
    font-size: 36px; line-height: 43px;
  }
  .service-intro {
    position: absolute; left: 430px; top: 491px; width: 340px;
    color: var(--body-gray); font-size: 15.4px; line-height: 18.2px;
  }
  .service-list { position: absolute; left: 427px; top: 590px; list-style: none; }
  .service-item { display: flex; align-items: flex-start; height: 96.5px; }
  .service-icon {
    flex: none; width: 63px; height: 63px; border-radius: 50%;
    background: var(--navy); margin-top: 4px;
    display: flex; align-items: center; justify-content: center;
  }
  .service-text {
    margin-left: 20px; width: 260px;
    color: var(--body-gray); font-size: 15.4px; line-height: 18.2px;
  }

  /* Right panel */
  .right-panel { position: absolute; left: 800px; top: 0; width: 400px; height: 928px; background: var(--teal); }
  .virus-photo {
    position: absolute; left: 0; top: 0; width: 400px; height: 766px;
    border-radius: 0 0 0 72px;
    background: radial-gradient(circle at 75% 30%, #7a7978 0%, #5a5959 40%, #4a4949 75%),
                var(--panel-dark);
  }
  .covid-pill {
    position: absolute; left: 0; top: 76px; width: 298px; height: 161px;
    background: var(--teal); border-radius: 0 80px 80px 0;
  }
  .covid-title {
    left: 37px; top: 15px; color: var(--white);
    font-size: 38px; line-height: 45.5px;
  }
  .covid-copy {
    position: absolute; left: 37px; top: 261px; width: 350px; white-space: nowrap;
    color: var(--white); font-size: 18.3px; line-height: 21.8px;
  }
  .covid-list { position: absolute; left: 37px; top: 467px; list-style: none; width: 350px; }
  .covid-item { position: relative; padding-left: 49px; height: 69.6px; white-space: nowrap; color: var(--white); font-size: 18.3px; line-height: 21.8px; }
  .covid-item::before {
    content: ""; position: absolute; left: 1px; top: 7px;
    width: 26px; height: 26px; border-radius: 50%; background: var(--teal);
  }
  .contact-call {
    left: 37px; top: 812px; color: var(--white);
    font-size: 18px; line-height: 21.5px;
  }
</style>
</head>
<body>
<main class="brochure">

  <h1 class="headline safety-title">All<br>For<br>Your<br>Safety</h1>

  <section class="care-photo" role="img" aria-label="Photo of a medical professional in mask and protective gear, tinted teal">
    <div class="care-copy">
      <p>Lorem ipsum dolor sit amet, consectetur adipiscing elit. Vivamus urna metus, iaculis eu turpis eget, porta consectetur felis. Nulla vel libero in sem mattis maximus sed at tellus. Aenean sem neque, consequat ultricies sollicitudin sed, dignissim eu justo. Nunc pellentesque, risus eu ultricies gravida, ante velit rutrum tellus, in vestibulum neque dui sed ligula.</p>
      <p>Orci varius natoque penatibus et magnis dis parturient montes, nascetur ridiculus mus. Ut id enim ac ligula facilisis vehicula. Ut mollis metus purus, sit amet vulputate neque tincidunt et. Phasellus pellentesque libero ante. Cras efficitur ullamcorper ultrices. Nullam elementum feugiat pharetra. Morbi tincidunt, ante ut semper efficitur, nisi lacus imperdiet enim, consectetur facilisis nisi orci id</p>
    </div>
  </section>

  <div class="pill-pattern" role="img" aria-label="Decorative pattern of vertical rounded bars in gray and navy"></div>

  <div class="brand-pill">
    <span class="brand-dot"></span>
    <span class="brand-name">Arven Medical Services</span>
  </div>

  <h2 class="headline service-title">Professionals<br>at your<br>service</h2>
  <p class="service-intro">Arven Medical Services offers a variety of services from emergency first aid to large scale screening for businesses with large office areas and events.</p>

  <ul class="service-list">
    <li class="service-item">
      <span class="service-icon">
        <svg width="44" height="44" viewBox="0 0 44 44" fill="#fff" stroke="#fff" stroke-width="2">
          <circle cx="22" cy="22" r="9" stroke="none"/>
          <line x1="22" y1="5" x2="22" y2="39"/><line x1="5" y1="22" x2="39" y2="22"/>
          <line x1="10" y1="10" x2="34" y2="34"/><line x1="34" y1="10" x2="10" y2="34"/>
          <circle cx="22" cy="5" r="3" stroke="none"/><circle cx="22" cy="39" r="3" stroke="none"/>
          <circle cx="5" cy="22" r="3" stroke="none"/><circle cx="39" cy="22" r="3" stroke="none"/>
          <circle cx="10" cy="10" r="3" stroke="none"/><circle cx="34" cy="34" r="3" stroke="none"/>
          <circle cx="34" cy="10" r="3" stroke="none"/><circle cx="10" cy="34" r="3" stroke="none"/>
        </svg>
      </span>
      <p class="service-text">Lorem ipsum dolor sit amet, consectetur adipiscing elit. Vivamus urna metus, iaculis eu turpis eget, porta consectetur felis.</p>
    </li>
    <li class="service-item">
      <span class="service-icon">
        <svg width="40" height="40" viewBox="0 0 40 40" fill="none" stroke="#fff" stroke-width="3" stroke-linecap="round">
          <path d="M28 6 L34 12 L16 30 L10 24 Z" fill="#fff"/>
          <line x1="10" y1="30" x2="5" y2="35"/>
        </svg>
      </span>
      <p class="service-text">Lorem ipsum dolor sit amet, consectetur adipiscing elit. Vivamus urna metus, iaculis eu turpis eget, porta consectetur felis.</p>
    </li>
    <li class="service-item">
      <span class="service-icon">
        <svg width="42" height="42" viewBox="0 0 42 42">
          <rect x="15" y="5" width="12" height="7" rx="2" fill="none" stroke="#fff" stroke-width="3"/>
          <rect x="4" y="11" width="34" height="25" rx="5" fill="#fff"/>
          <rect x="18" y="16" width="6" height="15" fill="#253589"/>
          <rect x="13.5" y="20.5" width="15" height="6" fill="#253589"/>
        </svg>
      </span>
      <p class="service-text">Lorem ipsum dolor sit amet, consectetur adipiscing elit. Vivamus urna metus, iaculis eu turpis eget, porta consectetur felis.</p>
    </li>
  </ul>

  <section class="right-panel">
    <div class="virus-photo" role="img" aria-label="Grayscale close-up photo of coronavirus particles"></div>
    <div class="covid-pill">
      <h2 class="headline covid-title">New<br>Covid-19<br>Services</h2>
    </div>
    <p class="covid-copy">Lorem ipsum dolor sit amet,<br>consectetur adipiscing elit. Vivamus<br>urna metus, iaculis eu turpis eget,<br>porta consectetur felis. Nulla vel libero<br>in sem mattis maximus sed at tellus.<br>Aenean sem neque, consequat<br>ultricies sollicitudin sed, dignissim eu<br>justo. Nunc pellentesque, risus eu</p>
    <ul class="covid-list">
      <li class="covid-item">Lorem ipsum dolor sit amet,<br>consectetur adipiscing elit.</li>
      <li class="covid-item">Vivamus urna metus, iaculis eu<br>turpis eget, porta consectetur</li>
      <li class="covid-item">Nulla vel libero in sem mattis<br>maximus sed at tellus.</li>
      <li class="covid-item">Aenean sem neque, consequat<br>ultricies sollicitudin sed,</li>
    </ul>
    <p class="headline contact-call">Contact us now to make<br>your workplace safe from<br>Covid-19</p>
  </section>

</main>
</body>
</html>
```